Sticker to put on shipping boxes-Pet ProductDelivery

I am looking for a sticker to put on the exterior of brown shipping boxes. We deliver pet products to a local consumer base and if our clients are not home, we leave the products on the door step. We would like to place a sticker on the box so that when looking at the box the consumer knows it came from us.

Looking for a design that is not larger than about a 3x5 or 5x5? I want it large enough to stand out, yet not so large that it is overwhelming. It also does not have to be square. It can also be rectangle. It will be placed in a bottom corner.

The design need to stand out on a brown box.

Attached is our logo for you to play around with.

Take note that the file with our slogan has colors mixes up.

The words 'Premium Pet Products' should be the same gray and the word 'Pet'. And the word 'Delivered' the same color as the word 'Brisk'.

Target Market(s)

Audience is mid 20's to seniors in senior living complexes. Those interested in convince and too buy to shop for themselves.

Industry/Entity Type

Shipping

Requirements
Must have
• Color but not overwhelming.

Orange, green, blue to match the logo colors.
Should not have
• Does not need to have a lot of text. Focus more on the Brisk Hound name and logo.

```html
<!DOCTYPE html>
<html lang="en">
<head>
<meta charset="utf-8">
<title>Brisk Hound – Box Sticker</title>
<link rel="stylesheet" href="https://fonts.googleapis.com/css2?family=Ubuntu:ital,wght@0,400;1,300&display=swap">
<style>
  :root {
    --page: #ffffff;
    --sticker-green: #d9e7ad;
    --frame-line: #ffffff;
    --accent-orange: #e8ad3b;
    --accent-blue: #4fb2d7;
    --mark-grey: #6d6a6a;
    --soft-grey: #a9a8ad;
    --faint-pattern: rgba(255, 255, 255, 0.28);
  }
  * { box-sizing: border-box; margin: 0; padding: 0; }
  html, body {
    width: 1200px;
    height: 1200px;
    overflow: hidden;
    background: var(--page);
  }
  .sticker {
    position: absolute;
    left: 54px;
    top: 48px;
    width: 1089px;
    height: 1090px;
    background: var(--sticker-green);
    overflow: hidden;
  }
  .sticker__frame {
    position: absolute;
    left: 26px;
    top: 24px;
    width: 1039px;
    height: 1040px;
    border: 2px solid var(--frame-line);
  }
  .sticker__bubbles {
    position: absolute;
    inset: 0;
    width: 100%;
    height: 100%;
  }
  .paw-pattern {
    position: absolute;
    background: var(--faint-pattern);
    border-radius: 40%;
    filter: blur(6px);
  }
  .paw-pattern--upper { left: 60px; top: 40px; width: 420px; height: 620px; opacity: 0.45; }
  .paw-pattern--corner { left: 740px; top: 560px; width: 349px; height: 530px; opacity: 0.55; border-radius: 50% 0 0 0; }
  .brand {
    position: absolute;
    left: 54px;
    top: 716px;
    display: flex;
    align-items: center;
    gap: 24px;
  }
  .brand__dot {
    width: 112px;
    height: 112px;
    border-radius: 50%;
    background: var(--mark-grey);
    flex: none;
  }
  .brand__name {
    font-family: "Ubuntu", sans-serif;
    font-weight: 400;
    font-size: 104px;
    line-height: 1;
    letter-spacing: 1px;
    color: var(--mark-grey);
    white-space: nowrap;
  }
  .tagline {
    position: absolute;
    left: 54px;
    top: 982px;
    font-family: "Ubuntu", sans-serif;
    font-style: italic;
    font-weight: 300;
    font-size: 45px;
    letter-spacing: 0.5px;
    color: var(--soft-grey);
    white-space: nowrap;
  }
  .tagline__highlight { color: var(--mark-grey); }
</style>
</head>
<body>
  <main class="sticker">
    <div class="paw-pattern paw-pattern--upper" role="img" aria-label="Faint paw print pattern"></div>
    <div class="paw-pattern paw-pattern--corner" role="img" aria-label="Large faint paw print"></div>

    <svg class="sticker__bubbles" viewBox="0 0 1089 1090" aria-hidden="true">
      <circle cx="732" cy="46" r="234" fill="var(--accent-orange)"/>
      <circle cx="978" cy="200" r="312" fill="var(--accent-blue)" opacity="0.94"/>
    </svg>

    <div class="sticker__frame"></div>

    <div class="brand">
      <span class="brand__dot"></span>
      <span class="brand__name">Brisk Hound</span>
    </div>

    <p class="tagline">PREMIUM PET PRODUCTS <span class="tagline__highlight">DELIVERED</span></p>
  </main>
</body>
</html>
```